Website incl. html for real estate project

We need the design and implementation of a website for a real estate project. Condominiums are built, which are sold.
We upload the sales brochure. The website should be based on the design of the sales brochure.
There are three houses with 5 apartments each. It should be rendered like this. The structure of the menu should be roughly as follows. Most information about the content is either in the appendix as a picture or in the brochure (PDF)):
Home (page 4-5 from the brochure)
House A
house B
house c
overview
basement
Municipal elections (page 6-7 in the brochure pdf)
Contact
Please use Roboto Regular as font.
And one page should give an overview of all apartments with the prices, the living space, etc. as on the file overview2.jpg.
If you go to the House A, House B, or House C menus, a page should come up with the details for that house only. The pages in the brochure are:
House A (Page 10-11)
House B (page 22-23)
House C (page 34-35)
The individual apartments should each be shown on a property page. There the plan / floor plan of the apartment and the pictures from the inside should be shown. As with the object page.jpg attachment.
Für die Designer... Mehr Zeit...
Coded - Design and coding required
1 page

```html
<!DOCTYPE html>
<html lang="en">
<head>
<meta charset="utf-8">
<title>Residential Park to the Ahorn</title>
<link href="https://fonts.googleapis.com/css2?family=Roboto:wght@300;400;500;700&display=swap" rel="stylesheet">
<style>
:root{
  --blue:#1583d0;
  --blue-band:#0d87d3;
  --red:#d2232a;
  --ink:#1f2a33;
  --text:#4a4f55;
  --muted:#6b7177;
  --grey-band:#e8e8e8;
  --footer:#1c2833;
  --line:#d6d9dc;
  --white:#ffffff;
}
*{box-sizing:border-box;margin:0;padding:0}
html,body{width:1200px;height:4478px;overflow:hidden}
body{font-family:'Roboto',sans-serif;color:var(--text);background:var(--white);position:relative}

/* header */
.site-header{position:absolute;top:0;left:0;width:1200px;height:113px;background:var(--white)}
.brand{position:absolute;left:110px;top:40px;display:flex;align-items:center;gap:10px;color:var(--blue);font-weight:500}
.brand-mark{width:14px;height:14px;background:var(--blue)}
.brand-name{font-size:27px;letter-spacing:1px;line-height:1}
.brand-sub{font-size:13px;letter-spacing:4px;display:block;margin-top:4px}
.top-contact{position:absolute;right:110px;top:26px;font-size:15px;color:var(--ink);display:flex;gap:12px;align-items:center}
.top-contact svg{width:13px;height:13px;fill:var(--blue);vertical-align:-1px;margin-right:4px}
.main-nav{position:absolute;right:110px;top:74px;display:flex;gap:19px;font-size:15.5px;color:var(--ink)}
.main-nav .active{color:var(--blue)}

/* hero */
.hero{position:absolute;top:113px;left:0;width:1200px;height:650px}
.hero-photo{position:absolute;inset:0;background:linear-gradient(180deg,#eef1f2 0%,#d9dcd8 30%,#b9bcb6 48%,#6f8f4e 62%,#3e6a2a 100%)}
.house-label{position:absolute;font-size:18px;font-weight:500;color:#111}
.hero svg{position:absolute;left:0;top:0}

/* intro */
.intro-title{position:absolute;left:110px;top:705px;font-size:40px;line-height:52px;font-weight:500;color:var(--ink);text-transform:uppercase}
.intro-copy{position:absolute;left:110px;top:834px;width:500px;font-size:15px;line-height:26px;color:var(--text);font-weight:300}
.intro-copy p{margin-bottom:26px}
.btn-outline{position:absolute;left:110px;top:1150px;width:147px;height:58px;border:1px solid var(--ink);display:flex;align-items:center;justify-content:center;font-size:16px;font-weight:500;color:var(--ink)}
.intro-photo{position:absolute;left:653px;top:783px;width:436px;height:503px;background:linear-gradient(135deg,#f1f1ef 0%,#dfe2e2 55%,#b9bdbe 100%)}

.stats{position:absolute;left:110px;top:1259px;width:860px;height:157px;background:var(--white);box-shadow:0 4px 18px rgba(0,0,0,.08);display:flex;align-items:center}
.stats .arrow{position:absolute;top:68px;width:12px;height:20px;stroke:#9aa0a6;fill:none;stroke-width:2}
.stat{display:flex;gap:12px;align-items:flex-start;padding:0 15px}
.stat+.stat{border-left:1px solid var(--line)}
.stat svg{width:80px;height:64px;stroke:var(--ink);fill:none;stroke-width:2.2}
.stat svg .acc{stroke:var(--blue)}
.stat-num{font-size:40px;font-weight:500;color:var(--blue);line-height:44px}
.stat-label{font-size:15px;line-height:22px;color:var(--text)}

/* overview */
.overview{position:absolute;top:1492px;left:0;width:1200px;height:778px;background:var(--grey-band)}
.section-title{position:absolute;left:0;width:1200px;text-align:center;font-size:40px;font-weight:500;color:var(--ink);text-transform:uppercase}
.plan{position:absolute;left:92px;top:157px;width:1016px;height:556px;background:linear-gradient(180deg,#f4f4f3,#eceeea);border:1px solid #dcdcdc}

/* houses */
.houses{position:absolute;top:2270px;left:0;width:1200px;height:1148px;background:var(--white)}
.slide-band{position:absolute;left:0;top:161px;width:1200px;height:348px;background:linear-gradient(180deg,#f4f5f4 0%,#e7e9e6 60%,#dfe6d8 100%);opacity:.9}
.slide-main{position:absolute;left:313px;top:138px;width:576px;height:395px;background:linear-gradient(180deg,#eef2f4 0%,#cfd2cd 35%,#8f928c 58%,#5c7f3c 78%,#3f6528 100%);box-shadow:0 4px 14px rgba(0,0,0,.12)}
.house-title{position:absolute;left:0;width:1200px;top:600px;text-align:center;font-size:28px;font-weight:400;color:var(--ink)}
.house-copy{position:absolute;left:205px;top:650px;width:790px;text-align:center;font-size:15px;line-height:26.5px;font-weight:300}
.units{position:absolute;left:219px;top:791px;width:764px;border:1px solid #c9ccd0;border-radius:6px;overflow:hidden;border-collapse:separate;border-spacing:0;font-size:15px;color:var(--text)}
.units td{height:56px;padding:0 30px;border-bottom:1px solid #c9ccd0;border-right:1px solid #c9ccd0;line-height:18px}
.units td:last-child{border-right:none}
.units tr:last-child td{border-bottom:none}
.units tr:nth-child(even) td{background:#f6f7f8}

/* contact */
.contact{position:absolute;top:3418px;left:0;width:1200px;height:625px;background:var(--blue-band);color:var(--white)}
.contact .section-title{color:var(--white);top:52px}
.map{position:absolute;left:110px;top:145px;width:441px;height:393px;background:linear-gradient(135deg,#b8d3f0 0%,#dfe5ea 45%,#a9c7ea 100%)}
.form{position:absolute;left:593px;top:145px;width:496px}
.form h3{font-size:22px;font-weight:500;margin-bottom:16px}
.form p{font-size:15px;line-height:26px;font-weight:300;margin-bottom:24px}
.field{background:var(--white);color:var(--muted);font-size:15px;padding:0 16px;display:flex;align-items:center}
.row{display:flex;gap:10px;margin-bottom:10px}
.row .field{flex:1;height:50px}
.field.area{height:140px;align-items:flex-start;padding-top:18px}
.btn-light{margin-top:24px;width:162px;height:58px;border:1px solid var(--white);display:flex;align-items:center;justify-content:center;font-size:17px;font-weight:500}

/* footer */
.site-footer{position:absolute;top:4043px;left:0;width:1200px;height:435px;background:var(--footer);color:var(--white)}
.footer-col{position:absolute;top:52px}
.footer-col h4{font-size:21px;font-weight:500;margin-bottom:16px}
.footer-col ul{list-style:none;font-size:15px;line-height:26.6px}
.social li{display:flex;align-items:center;gap:10px;margin-bottom:26px;line-height:18px}
.social .sq{width:14px;height:14px;border:2px solid var(--white);border-radius:3px}
.news p{font-size:15px;margin-bottom:22px}
.news-input{display:flex;width:494px;height:52px}
.news-input .field{flex:1;font-size:16px}
.news-input .send{width:50px;background:var(--blue);display:flex;align-items:center;justify-content:center}
.news-input svg{width:20px;height:20px;fill:var(--white)}
.footer-rule{position:absolute;left:110px;top:354px;width:979px;height:1px;background:#3a4652}
.copyright{position:absolute;left:0;top:380px;width:1200px;text-align:center;font-size:15px;font-weight:300}
</style>
</head>
<body>

<header class="site-header">
  <div class="brand">
    <span class="brand-mark"></span>
    <span><span class="brand-name">BRUNNWALD</span><span class="brand-sub">IMMOBILIEN AG</span></span>
  </div>
  <div class="top-contact">
    <span><svg viewBox="0 0 24 24"><path d="M6.6 10.8a15 15 0 006.6 6.6l2.2-2.2c.3-.3.7-.4 1-.2 1.1.4 2.3.6 3.6.6.6 0 1 .4 1 1V20c0 .6-.4 1-1 1A17 17 0 013 4c0-.6.4-1 1-1h3.5c.6 0 1 .4 1 1 0 1.3.2 2.5.6 3.6.1.3 0 .7-.2 1z"/></svg>+41 61 555 01 20</span>
    <span>|</span>
    <span><svg viewBox="0 0 24 24"><path d="M2 5h20v14H2z M2 5l10 8 10-8" /></svg>info@parkresidenz-ahorn.ch</span>
  </div>
  <nav class="main-nav">
    <span class="active">Home</span><span>House A</span><span>House B</span><span>House C</span><span>Overview</span><span>Basement</span><span>Municipal Elections</span><span>Contact</span>
  </nav>
</header>

<section class="hero">
  <div class="hero-photo" role="img" aria-label="Rendering of the three residential buildings with lawn, trees and people in front"></div>
  <span class="house-label" style="left:168px;top:141px">House C</span>
  <span class="house-label" style="left:601px;top:196px">House B</span>
  <span class="house-label" style="left:822px;top:155px">House A</span>
  <svg width="1200" height="650" viewBox="0 0 1200 650">
    <polygon points="0,650 0,612 209,421 713,635 1200,639 1200,650" fill="#fff"/>
    <polyline points="0,612 209,421 713,635 1200,639" fill="none" stroke="#d2232a" stroke-width="4"/>
  </svg>
</section>

<h1 class="intro-title">Residential Park to<br>the Ahorn</h1>
<div class="intro-copy">
  <p>The superstructure with three apartment buildings and a total of 15 condominiums is being built between Talackerstrasse and Moosmattweg in Erlenbach near Birsau.</p>
  <p>The modern, high-quality apartments face the quiet Moosmatt district and the beautiful view of the green "Hohberg".</p>
  <p>The apartments are in an ideal location in Erlenbach with good sun exposure and the nearest bus stop is just 120 meters away. The apartments are equipped with a spacious balcony on the upper floor and a covered patio and private garden on the ground floor.</p>
</div>
<div class="btn-outline">READ MORE</div>
<div class="intro-photo" role="img" aria-label="Bright bedroom interior with desk, curtain and bed"></div>

<div class="stats">
  <svg class="arrow" style="left:10px" viewBox="0 0 12 20"><polyline points="10,2 2,10 10,18"/></svg>
  <svg class="arrow" style="right:10px" viewBox="0 0 12 20"><polyline points="2,2 10,10 2,18"/></svg>
  <div class="stat" style="margin-left:30px;width:280px">
    <svg viewBox="0 0 80 64"><polyline points="4,32 26,10 48,32"/><rect x="10" y="28" width="32" height="28"/><rect x="22" y="40" width="8" height="16"/><circle class="acc" cx="58" cy="30" r="14"/><path class="acc" d="M62 24h-5a3 3 0 000 6h2a3 3 0 010 6h-5M58 20v20"/></svg>
    <div><div class="stat-num">3</div><div class="stat-label">Building with<br>individual housing offer</div></div>
  </div>
  <div class="stat" style="width:232px">
    <svg viewBox="0 0 80 64"><rect x="6" y="10" width="44" height="44"/><path d="M6 32h18v22M30 10v14h20"/><path class="acc" d="M62 10v44M56 16l6-6 6 6M56 48l6 6 6-6"/></svg>
    <div><div class="stat-num">9</div><div class="stat-label">Different<br>floor plan types</div></div>
  </div>
  <div class="stat" style="width:300px">
    <svg viewBox="0 0 80 64"><path class="acc" d="M4 20L36 6l32 14"/><path d="M14 38l5-12h34l5 12v14H14z"/><path d="M14 38h44M20 46h6M46 46h6"/></svg>
    <div><div class="stat-num">27</div><div class="stat-label">Parking spaces in the<br>underground car park</div></div>
  </div>
</div>

<section class="overview">
  <h2 class="section-title" style="top:64px">Overview Plan</h2>
  <div class="plan" role="img" aria-label="Site plan showing Haus A, Haus B and Haus C between Moosmattweg and Talackerstrasse"></div>
</section>

<section class="houses">
  <h2 class="section-title" style="top:56px">The Houses</h2>
  <div class="slide-band" role="img" aria-label="Faded renderings of the neighbouring houses"></div>
  <div class="slide-main" role="img" aria-label="Rendering of House A with terraces, garden and parasol"></div>
  <h3 class="house-title">Residential Park zum Ahorn House A</h3>
  <p class="house-copy">The "House A" building has five modern apartments with individual floor plans. All apartments have a spacious outdoor area with a balcony or a covered patio facing south towards the Hohberg, the local mountain in Erlenbach. The living rooms are equipped with large windows, which fill the rooms with sunlight flooded. The building is accessible directly from the underground car park with the lift.</p>
  <table class="units">
    <tr><td>Attic apartment</td><td>4.5 Zimmer</td><td>108 m2 of living space</td><td>105 m2 large sun terrace!</td></tr>
    <tr><td>Upper floor</td><td>3.5 Zimmer</td><td>81 m2 of living space</td><td>16 m2 balcony</td></tr>
    <tr><td>Upper Floor</td><td>4.5 Zimmer</td><td>102 m2 of living space</td><td>33 m2 balcony</td></tr>
    <tr><td>Ground floor</td><td>3.5 Zimmer</td><td>81 m2 of living space</td><td>16 m2 covered seating and<br>over 120 m² of garden</td></tr>
    <tr><td>Ground floor</td><td>4.5 Zimmer</td><td>102 m2 of living space</td><td>33 m2 covered seating and<br>over 120 m² of garden</td></tr>
  </table>
</section>

<section class="contact">
  <h2 class="section-title">Contact</h2>
  <div class="map" role="img" aria-label="Street map with location pin"></div>
  <div class="form">
    <h3>Write us</h3>
    <p>Lorem ipsum dolor sit amet, consectetur adipiscing elit, sed do eiusmod tempor incididunt ut labore et dolore.</p>
    <div class="row"><div class="field">Name*</div><div class="field">Email*</div></div>
    <div class="field area">Comment</div>
    <div class="btn-light">GET IN TOUCH</div>
  </div>
</section>

<footer class="site-footer">
  <div class="footer-col" style="left:110px">
    <h4>Sitemap</h4>
    <ul><li>Home</li><li>House A</li><li>House B</li><li>House C</li><li>Overview</li><li>Basement</li><li>Municipal Elections</li><li>Impressum</li><li>Privacy</li></ul>
  </div>
  <div class="footer-col social" style="left:359px">
    <h4>Social Media</h4>
    <ul><li><span class="sq"></span>Photostream</li><li><span class="sq"></span>Neighbourly</li></ul>
  </div>
  <div class="footer-col news" style="left:574px">
    <h4>Newsletter</h4>
    <p>Enter your email address to get information about us</p>
    <div class="news-input"><div class="field">Email Address</div><div class="send"><svg viewBox="0 0 24 24"><path d="M2 12L22 3l-5 18-5-7z"/></svg></div></div>
  </div>
  <div class="footer-rule"></div>
  <div class="copyright">Copyright © 2022, Brunnwald. All rights reserved.</div>
</footer>

</body>
</html>
```